marble ridge yard works
cards+letter head+envelopes+signs
marble ridge yard works -
Creative Brief
Use specific fonts
you deside
Simple
Lou Kettering
owner/operator
42 willow ave w po box 953 st.jacobs, on n0b 2n0
lou@marbleridge-example.ca
www.marbleridge-example.ca
professional member of greenscape guild. (they have a logo for this)
plain or watermark my log or just my brand mark.

```html
<!DOCTYPE html>
<html lang="en">
<head>
<meta charset="utf-8">
<title>Marble Ridge Yard Works – Stationery</title>
<link href="https://fonts.googleapis.com/css2?family=Montserrat:wght@400;600;700&display=swap" rel="stylesheet">
<style>
:root{
  --green:#3d9a2b;
  --green-dark:#2a7a1c;
  --green-light:#8cc63f;
  --ink:#555;
  --muted:#777;
  --line:#cfcfcf;
  --paper:#fff;
  --bg:#fff;
}
*{box-sizing:border-box;margin:0;padding:0}
html,body{width:1200px;height:504px;overflow:hidden;background:var(--bg)}
body{position:relative;font-family:'Montserrat',sans-serif;color:var(--ink)}
.piece{position:absolute;background:var(--paper);box-shadow:0 2px 6px rgba(0,0,0,.18);overflow:hidden}
.band{position:absolute;left:0;right:0;bottom:0;height:10px;background:linear-gradient(90deg,var(--green-dark),var(--green-light) 60%,var(--green))}

.logo{display:flex;align-items:center;gap:5px}
.logo-dot{width:10px;height:10px;border-radius:50%;background:var(--green);flex:none}
.logo-name{font-weight:700;font-size:11px;letter-spacing:.3px;color:var(--green);white-space:nowrap;line-height:1.1}
.logo-tag{font-size:5px;color:#888;letter-spacing:.5px;margin-top:1px;white-space:nowrap}
.logo.sm{gap:3px}
.logo.sm .logo-dot{width:6px;height:6px}
.logo.sm .logo-name{font-size:7px}
.logo.sm .logo-tag{font-size:3.5px}

.small{font-size:5px;line-height:7px;color:var(--muted)}
.watermark{position:absolute;border-radius:50%;background:var(--green-light);opacity:.12}

/* fax */
.fax{left:12px;top:12px;width:324px;height:461px}
.fax-title{position:absolute;right:18px;top:24px;font-size:14px;font-weight:600;letter-spacing:1px;color:#666}
.fax-table{position:absolute;left:18px;top:44px;width:292px;border-collapse:collapse}
.fax-table td{border:1px solid var(--line);font-size:5px;height:13px;padding:0 3px}
.fax-table td.lbl{background:#e6e6e6;width:36px}
.fax-checks{position:absolute;left:18px;top:102px;display:flex;gap:14px;font-size:5px}
.fax-checks span::before{content:"";display:inline-block;width:5px;height:5px;border:1px solid #999;margin-right:2px;vertical-align:-1px}
.fax-comments{position:absolute;left:18px;top:118px;font-size:5px}

/* envelopes */
.env-back{left:353px;top:12px;width:343px;height:113px}
.env-front{left:353px;top:137px;width:343px;height:151px}
.env-small{left:353px;top:312px;width:343px;height:151px}
.env-fold{position:absolute;top:0;left:0}
.env-back .logo{position:absolute;left:130px;top:64px}
.env-front .logo,.env-small .logo{position:absolute;left:14px;top:12px}
.env-addr{position:absolute;left:14px;top:40px;color:var(--green)}
.env-small .env-addr{top:auto;bottom:20px}

/* letterhead */
.letter{left:713px;top:12px;width:319px;height:461px}
.letter .logo{position:absolute;left:18px;top:16px}
.letter .contact{position:absolute;left:148px;top:18px;width:160px}
.letter .watermark{left:110px;top:165px;width:90px;height:90px}

/* cards */
.card{width:149px;height:77px}
.card.green{background:linear-gradient(135deg,var(--green-dark),var(--green-light))}
.card.green .logo{position:absolute;left:30px;top:30px}
.card.green .logo-name,.card.green .logo-tag{color:#fff}
.card.green .logo-dot{background:#fff}
.card-back .logo{position:absolute;left:8px;top:14px}
.card-back .contact{position:absolute;left:84px;top:12px;width:60px;font-size:4.5px;line-height:6px;overflow-wrap:anywhere}
.card-back .contact b{color:var(--ink)}
.card-tilted{left:884px;top:284px}
.c1{left:1039px;top:12px}
.c2{left:1039px;top:96px}
.c3{left:1039px;top:180px}
.c4{left:1039px;top:268px}
.c5{left:1039px;top:356px}
.c5 .wave{position:absolute;left:0;bottom:0}
</style>
</head>
<body>

<section class="piece fax">
  <div class="fax-title">FAX</div>
  <table class="fax-table">
    <tr><td class="lbl">To:</td><td></td><td class="lbl">From:</td><td></td></tr>
    <tr><td class="lbl">Fax:</td><td></td><td class="lbl">Pages:</td><td></td></tr>
    <tr><td class="lbl">Phone:</td><td></td><td class="lbl">Date:</td><td></td></tr>
    <tr><td class="lbl">Re:</td><td></td><td class="lbl">CC:</td><td></td></tr>
  </table>
  <div class="fax-checks">
    <span>Urgent</span><span>For Review</span><span>Please Comment</span><span>Please Reply</span><span>Please Recycle</span>
  </div>
  <div class="fax-comments">Comments:</div>
  <div class="band"></div>
</section>

<section class="piece env-back">
  <svg class="env-fold" width="343" height="60"><path d="M0 0 L171 55 L343 0" fill="none" stroke="#ddd" stroke-width="1"/></svg>
  <div class="logo"><span class="logo-dot"></span><div><div class="logo-name">MARBLERIDGE</div><div class="logo-tag">YARD WORKS</div></div></div>
</section>

<section class="piece env-front">
  <div class="logo"><span class="logo-dot"></span><div><div class="logo-name">MARBLERIDGE</div><div class="logo-tag">YARD WORKS</div></div></div>
  <div class="env-addr small">42 willow ave w po box 953<br>st.jacobs, on n0b 2n0</div>
</section>

<section class="piece env-small">
  <div class="logo"><span class="logo-dot"></span><div><div class="logo-name">MARBLERIDGE</div><div class="logo-tag">YARD WORKS</div></div></div>
  <div class="env-addr small">42 willow ave w po box 953 st.jacobs, on n0b 2n0</div>
</section>

<section class="piece letter">
  <div class="logo"><span class="logo-dot"></span><div><div class="logo-name">MARBLERIDGE</div><div class="logo-tag">YARD WORKS</div></div></div>
  <div class="contact small">42 willow ave w po box 953 st.jacobs, on n0b 2n0<br>lou@marbleridge-example.ca<br>www.marbleridge-example.ca</div>
  <div class="watermark"></div>
  <div class="band"></div>
</section>

<section class="piece card green card-tilted">
  <div class="logo"><span class="logo-dot"></span><div><div class="logo-name">MARBLERIDGE</div><div class="logo-tag">YARD WORKS</div></div></div>
</section>

<section class="piece card card-back c1">
  <div class="logo sm"><span class="logo-dot"></span><div><div class="logo-name">MARBLERIDGE</div><div class="logo-tag">YARD WORKS</div></div></div>
  <div class="contact small"><b>Lou Kettering</b><br>owner/operator<br>lou@<br>marbleridge-example.ca</div>
</section>

<section class="piece card green c2">
  <div class="logo"><span class="logo-dot"></span><div><div class="logo-name">MARBLERIDGE</div><div class="logo-tag">YARD WORKS</div></div></div>
</section>

<section class="piece card card-back c3">
  <div class="logo sm"><span class="logo-dot"></span><div><div class="logo-name">MARBLERIDGE</div><div class="logo-tag">YARD WORKS</div></div></div>
  <div class="contact small"><b>Lou Kettering</b><br>owner/operator<br>www.<br>marbleridge-example.ca</div>
</section>

<section class="piece card green c4">
  <div class="logo"><span class="logo-dot"></span><div><div class="logo-name">MARBLERIDGE</div><div class="logo-tag">YARD WORKS</div></div></div>
</section>

<section class="piece card card-back c5">
  <div class="logo sm"><span class="logo-dot"></span><div><div class="logo-name">MARBLERIDGE</div><div class="logo-tag">YARD WORKS</div></div></div>
  <div class="contact small"><b>Lou Kettering</b><br>member,<br>greenscape guild</div>
  <svg class="wave" width="149" height="22"><path d="M0 12 Q50 2 100 12 T149 8 V22 H0Z" fill="var(--green)"/></svg>
</section>

</body>
</html>
```